Business Card Design

Company is a Commercial Building Company specialising in New Construction and existing refurbishments

Business

Contact Information for Business Card

Derek Halloway
Construction Manager
E Derek@ridgemarkbuilding.com.au
M 0400 215 397
Mail 14 Tarrington Loop Kestrel Bay WA 6198

```html
<!DOCTYPE html>
<html lang="en">
<head>
<meta charset="utf-8">
<title>Ridgemark Building &amp; Construction – Business Card</title>
<link href="https://fonts.googleapis.com/css2?family=Saira+Semi+Condensed:wght@300;400;700&display=swap" rel="stylesheet">
<style>
  :root {
    --stage: #ebebeb;
    --card: #ffffff;
    --cyan: #1aafd0;
    --orange: #f08a0e;
    --ink: #1f2a3c;
    --text: #2b2b2b;
    --font: "Saira Semi Condensed", "Arial Narrow", sans-serif;
  }
  * { box-sizing: border-box; margin: 0; padding: 0; }
  html, body { width: 1200px; height: 973px; overflow: hidden; }
  body {
    background: var(--stage);
    font-family: var(--font);
    position: relative;
  }
  .card {
    position: absolute;
    width: 540px;
    height: 330px;
    background: var(--card);
    box-shadow: 0 6px 18px rgba(0,0,0,0.12);
    overflow: hidden;
  }
  .card--front { left: 40px; top: 321px; }
  .card--back  { left: 620px; top: 321px; }
  .card__wedges { position: absolute; inset: 0; }
  .wedge--cyan { fill: var(--cyan); }
  .wedge--orange { fill: var(--orange); }

  .wordmark { position: absolute; color: var(--ink); line-height: 1; white-space: nowrap; }
  .wordmark__name { font-weight: 700; text-transform: uppercase; letter-spacing: 0.5px; }
  .wordmark__sub { font-weight: 300; text-transform: uppercase; letter-spacing: 0.5px; }

  .card--front .wordmark { left: 90px; top: 132px; }
  .card--front .wordmark__name { font-size: 30px; }
  .card--front .wordmark__sub { font-size: 25px; margin-top: 4px; }

  .card--back .wordmark { left: 130px; top: 196px; }
  .card--back .wordmark__name { font-size: 17px; }
  .card--back .wordmark__sub { font-size: 14px; margin-top: 1px; }

  .contact {
    position: absolute;
    left: 130px;
    top: 96px;
    color: var(--text);
    font-size: 15px;
    line-height: 1;
    white-space: nowrap;
  }
  .contact__name { font-weight: 700; text-transform: uppercase; color: var(--ink); font-size: 16px; }
  .contact__role { font-weight: 300; }
  .contact__list { list-style: none; margin-top: 8px; }
  .contact__item { display: flex; align-items: center; gap: 7px; margin-top: 6px; font-weight: 300; }
  .contact__icon { width: 13px; height: 13px; flex: none; }
  .contact__icon circle { fill: var(--ink); }
  .contact__icon .glyph { fill: #fff; stroke: none; }
</style>
</head>
<body>

<section class="card card--front" aria-label="Business card front">
  <svg class="card__wedges" viewBox="0 0 540 330" preserveAspectRatio="none" aria-hidden="true">
    <polygon class="wedge--cyan" points="0,0 120,0 0,210"/>
    <polygon class="wedge--orange" points="540,95 540,330 360,330"/>
  </svg>
  <div class="wordmark">
    <div class="wordmark__name">Ridgemark Building</div>
    <div class="wordmark__sub">&amp; Construction</div>
  </div>
</section>

<section class="card card--back" aria-label="Business card back">
  <svg class="card__wedges" viewBox="0 0 540 330" preserveAspectRatio="none" aria-hidden="true">
    <polygon class="wedge--cyan" points="0,0 215,0 0,190"/>
    <polygon class="wedge--orange" points="540,60 540,330 395,330"/>
  </svg>

  <div class="contact">
    <p><span class="contact__name">Derek Halloway</span> <span class="contact__role">| Construction Manager</span></p>
    <ul class="contact__list">
      <li class="contact__item">
        <svg class="contact__icon" viewBox="0 0 14 14" aria-hidden="true"><circle cx="7" cy="7" r="7"/><rect class="glyph" x="4.5" y="3" width="5" height="8" rx="1"/></svg>
        0400 215 397
      </li>
      <li class="contact__item">
        <svg class="contact__icon" viewBox="0 0 14 14" aria-hidden="true"><circle cx="7" cy="7" r="7"/><rect class="glyph" x="3.5" y="4.5" width="7" height="5"/></svg>
        Derek@ridgemarkbuilding.com.au
      </li>
      <li class="contact__item">
        <svg class="contact__icon" viewBox="0 0 14 14" aria-hidden="true"><circle cx="7" cy="7" r="7"/><path class="glyph" d="M7 3a2.6 2.6 0 0 1 2.6 2.6C9.6 7.6 7 11 7 11S4.4 7.6 4.4 5.6A2.6 2.6 0 0 1 7 3z"/></svg>
        14 Tarrington Loop Kestrel Bay WA 6198
      </li>
    </ul>
  </div>

  <div class="wordmark">
    <div class="wordmark__name">Ridgemark Building</div>
    <div class="wordmark__sub">&amp; Construction</div>
  </div>
</section>

</body>
</html>
```